Design some Business Cards

I need a business card that goes with my current website looks, i have a mockup which i am sending, the idea i have is to be very clean in the front, and in the back all my skills as developer, kind of vornexa skills.

My website si maltrevo.com

```html
<!DOCTYPE html>
<html lang="en">
<head>
<meta charset="utf-8">
<title>Mateo Rivas — Business Cards</title>
<link href="https://fonts.googleapis.com/css2?family=Quicksand:wght@500;600;700&display=swap" rel="stylesheet">
<style>
  :root{
    --bg:#ecebe8;
    --ink:#111111;
    --paper:#f7f7f7;
    --paper-shade:#dcdcdc;
    --steel-light:#e2e2e2;
    --steel-dark:#858585;
    --band:#141414;
    --band-fold:#3a3a3a;
    --band-tab:#5c5c5c;
    --white:#ffffff;
    --text-soft:#222222;
  }
  *{box-sizing:border-box;margin:0;padding:0}
  html,body{width:1200px;height:912px;overflow:hidden}
  body{background:var(--bg);font-family:"Quicksand",sans-serif;color:var(--ink);position:relative}

  .card{position:absolute;width:620px;height:354px;border-radius:4px;overflow:hidden;box-shadow:0 10px 28px rgba(0,0,0,.22)}

  /* Front */
  .card-front{left:40px;top:80px;background:linear-gradient(160deg,var(--steel-light) 0%,#bdbdbd 55%,var(--steel-dark) 100%)}
  .portrait{position:absolute;left:96px;top:150px;width:168px;height:168px;border-radius:50%;background:radial-gradient(circle at 50% 45%,#f4ecd2 0%,#e8dcb4 45%,#fafafa 75%);border:3px solid var(--white)}
  .bio{position:absolute;right:40px;top:34px;text-align:right;font-weight:600;font-size:17px;line-height:1.5;color:var(--text-soft)}
  .ribbon{position:absolute;left:0;top:0;width:620px;height:354px}
  .ribbon-url{position:absolute;left:330px;top:238px;width:260px;text-align:center;color:var(--white);font-weight:700;font-size:18px;letter-spacing:.3px}

  /* Back */
  .card-back{left:540px;top:478px;background:linear-gradient(165deg,var(--white) 0%,var(--paper) 60%,var(--paper-shade) 100%)}
  .name-tag{position:absolute;left:0;top:110px;background:var(--band);color:var(--white);padding:8px 22px 8px 28px;border-radius:0 10px 10px 0}
  .name{font-weight:700;font-size:30px;line-height:1}
  .role{font-weight:600;font-size:13px;text-align:right;margin-top:3px}
  .contacts{position:absolute;left:40px;top:190px;list-style:none}
  .contacts li{display:flex;align-items:center;gap:16px;font-weight:600;font-size:16px;height:32px}
  .contacts li:last-child{font-weight:700}
  .contacts svg{width:18px;height:18px;flex:none}
  .hire{position:absolute;right:28px;top:26px;text-align:right}
  .hire-title{font-weight:700;font-size:24px;margin-bottom:6px;padding-right:40px}
  .skills{list-style:none}
  .skills li{display:flex;justify-content:flex-end;align-items:center;gap:22px;font-weight:600;font-size:16px;height:29px}
  .skills li::after{content:"";width:15px;height:15px;border-radius:50%;background:var(--ink)}
</style>
</head>
<body>

<section class="card card-front">
  <div class="portrait" role="img" aria-label="Portrait photo of the developer"></div>
  <p class="bio">I'm from Mexico,<br>precisely Quelvaro<br>(nothing to do with the sauce).<br>I'm a 35 years old developer,<br>happily married with a<br>kid who's the love of my live.</p>
  <svg class="ribbon" viewBox="0 0 620 354" aria-hidden="true">
    <polygon points="300,248 330,226 330,300 300,300" fill="var(--band-fold)"/>
    <rect x="270" y="248" width="30" height="64" fill="var(--band-tab)"/>
    <polygon points="590,200 620,200 620,272 590,226" fill="var(--band-fold)"/>
    <rect x="330" y="226" width="260" height="74" fill="var(--band)"/>
    <polygon points="590,226 620,200 620,300 590,300" fill="var(--band)"/>
  </svg>
  <p class="ribbon-url">www.maltrevo.com</p>
</section>

<section class="card card-back">
  <div class="name-tag">
    <p class="name">Mateo Rivas</p>
    <p class="role">Web Designer</p>
  </div>
  <ul class="contacts">
    <li>
      <svg viewBox="0 0 24 24"><path d="M6.6 2.5l3 3.2-1.8 2.6c1.3 2.8 3.4 4.9 6.1 6.1l2.6-1.8 3.2 3-2 3.9C10.6 19.3 4.7 13.4 2.5 6.3z" fill="var(--ink)"/></svg>
      <span>+52 900 555 0147</span>
    </li>
    <li>
      <svg viewBox="0 0 24 24"><path d="M2 11L22 3 16 21 11 14z M11 14L22 3" fill="var(--ink)" stroke="var(--white)" stroke-width="1"/></svg>
      <span>hola@maltrevo.com</span>
    </li>
    <li>
      <svg viewBox="0 0 24 24" fill="none" stroke="var(--ink)" stroke-width="2"><circle cx="12" cy="12" r="9.5"/><ellipse cx="12" cy="12" rx="4" ry="9.5"/><path d="M2.5 12h19M4 7h16M4 17h16"/></svg>
      <span>maltrevo.com</span>
    </li>
    <li>
      <svg viewBox="0 0 24 24"><path d="M12 1.5a7 7 0 0 0-7 7c0 5.2 7 14 7 14s7-8.8 7-14a7 7 0 0 0-7-7z" fill="var(--ink)"/><circle cx="12" cy="8.5" r="2.6" fill="var(--white)"/></svg>
      <span>Palmera Area, Mexico</span>
    </li>
  </ul>
  <div class="hire">
    <p class="hire-title">Hire For</p>
    <ul class="skills">
      <li>HTML</li>
      <li>CSS</li>
      <li>Javascript</li>
      <li>TDD</li>
      <li>Ruby</li>
      <li>Rails</li>
      <li>Git</li>
    </ul>
  </div>
</section>

</body>
</html>
```